Stationary Design to Complement our Website

We would like template designed for word documents that we can use for headed paper. The template should complement the style of our website & incorporate our existing logo. https://www.palvenroutes.com/

The header and footer design should be sperate PNG or JPEG files that we can copy and paste into word header and footers. They should work on A4 & letter sized papers.

Note the main web colours are as follows:

Black
HEX code #2b2c2b
C=71 M=64 Y=64 K=65
RGB 43,44,43

Green
HEX code #116c49
C=88 M=33 Y=82 K=24
RGB 17,108,73

Current fonts are ALEO & Gilroy.

Fonts and colours in new design don't have to match website exactly but should be complementary.
Updates

Made some updates to the brief

Font styles to use
Serif

Requirements
Must have
• a simple design that complements our website.
Some kind of graphic on the top & some sort of graphic on the bottom. Not just plain logo on top.
designs that incorporate the clouds might look good
Can also incorporate 5* rate marsh rating
Should not have
• no photographs included on the design

```html
<!DOCTYPE html>
<html lang="en">
<head>
<meta charset="utf-8">
<title>Palven Routes – Letterhead Header &amp; Footer</title>
<link href="https://fonts.googleapis.com/css2?family=Cinzel:wght@400&family=Montserrat:wght@400&display=swap" rel="stylesheet">
<style>
  :root {
    --canvas: #000000;
    --paper: #ffffff;
    --green-deep: #0f7d1a;
    --green-mid: #2ea23f;
    --green-light: #4cc45a;
    --brand-green: #17704a;
    --ink: #111111;
    --text-grey: #4a4a4a;
    --white: #ffffff;
  }
  * { margin: 0; padding: 0; box-sizing: border-box; }
  html, body { width: 1200px; height: 1200px; overflow: hidden; background: var(--canvas); }
  .canvas { position: relative; width: 1200px; height: 1200px; background: var(--canvas); }

  .header-band {
    position: absolute; left: 101px; top: 316px; width: 992px; height: 256px;
    overflow: hidden;
  }
  .header-art {
    position: absolute; inset: 0;
    background:
      radial-gradient(circle at 84% 40%, rgba(120,240,140,.55) 0, rgba(90,220,110,.25) 10%, transparent 22%),
      radial-gradient(circle at 30% 85%, rgba(80,200,90,.6) 0, transparent 40%),
      linear-gradient(160deg, var(--green-deep) 0%, var(--green-mid) 55%, var(--green-deep) 100%);
  }
  .wordmark {
    position: absolute; display: flex; align-items: center;
    font-family: "Cinzel", serif; font-weight: 400; white-space: nowrap;
  }
  .wordmark-dot { display: block; border-radius: 50%; flex: none; }
  .header-band .wordmark { left: 135px; top: 118px; color: var(--white); font-size: 58px; letter-spacing: 9px; }
  .header-band .wordmark-dot { width: 40px; height: 40px; background: var(--white); margin-right: 30px; margin-top: -30px; }

  .footer-band {
    position: absolute; left: 101px; top: 648px; width: 992px; height: 254px;
    background: var(--paper);
  }
  .footer-band .wordmark { left: 57px; top: 98px; color: var(--ink); font-size: 50px; letter-spacing: 8px; }
  .footer-band .wordmark-dot { width: 34px; height: 34px; background: var(--brand-green); margin-right: 28px; margin-top: -28px; }

  .contact-list { position: absolute; left: 770px; top: 62px; list-style: none;
    font-family: "Montserrat", sans-serif; color: var(--text-grey); }
  .contact-item { position: absolute; left: 0; display: flex; align-items: flex-start; white-space: nowrap; }
  .contact-icon { width: 16px; height: 16px; flex: none; margin-right: 10px; }
  .contact-text { font-size: 11.5px; line-height: 14.5px; }
  .contact-text.small { font-size: 9.5px; line-height: 12px; }
  .item-phone { top: 0; }
  .item-mail { top: 52px; }
  .item-web { top: 77px; }
  .item-address { top: 100px; }
</style>
</head>
<body>
<main class="canvas">

  <section class="header-band" aria-label="Letterhead header">
    <div class="header-art" role="img" aria-label="Abstract green background with scattered dots, paint splashes and soft glowing bubbles"></div>
    <div class="wordmark"><span class="wordmark-dot"></span>Palven Routes</div>
  </section>

  <section class="footer-band" aria-label="Letterhead footer">
    <div class="wordmark"><span class="wordmark-dot"></span>Palven Routes</div>

    <ul class="contact-list">
      <li class="contact-item item-phone">
        <svg class="contact-icon" viewBox="0 0 16 16" aria-hidden="true">
          <rect width="16" height="16" rx="1.5" fill="var(--brand-green)"/>
          <path d="M4.5 4 L6.5 3.6 L7.4 5.8 L6.3 6.6 Q7.3 8.7 9.4 9.7 L10.2 8.6 L12.4 9.5 L12 11.5 Q7.5 11.8 4.5 4 Z" fill="#fff"/>
        </svg>
        <span class="contact-text">0800 014 5521<br>1877 402 6618<br>+353 61 40213</span>
      </li>
      <li class="contact-item item-mail">
        <svg class="contact-icon" viewBox="0 0 16 16" aria-hidden="true">
          <rect width="16" height="16" rx="1.5" fill="var(--brand-green)"/>
          <rect x="3" y="4.5" width="10" height="7" fill="none" stroke="#fff" stroke-width="1"/>
          <path d="M3 4.5 L8 8.5 L13 4.5 M3 11.5 L6.5 8 M13 11.5 L9.5 8" fill="none" stroke="#fff" stroke-width="1"/>
        </svg>
        <span class="contact-text">palvenroutes@email.com</span>
      </li>
      <li class="contact-item item-web">
        <svg class="contact-icon" viewBox="0 0 16 16" aria-hidden="true">
          <rect width="16" height="16" rx="1.5" fill="var(--brand-green)"/>
          <circle cx="8" cy="8" r="4.2" fill="none" stroke="#fff" stroke-width=".9"/>
          <ellipse cx="8" cy="8" rx="1.8" ry="4.2" fill="none" stroke="#fff" stroke-width=".8"/>
          <path d="M3.8 8 H12.2 M4.5 5.8 H11.5 M4.5 10.2 H11.5" stroke="#fff" stroke-width=".7"/>
        </svg>
        <span class="contact-text">www.palvenroutes.com</span>
      </li>
      <li class="contact-item item-address">
        <svg class="contact-icon" viewBox="0 0 16 16" aria-hidden="true">
          <rect width="16" height="16" rx="1.5" fill="var(--brand-green)"/>
          <path d="M8 3.2 L13 7.6 H11.5 V12.5 H4.5 V7.6 H3 Z" fill="#fff"/>
          <rect x="7" y="9.5" width="2" height="3" fill="var(--brand-green)"/>
        </svg>
        <span class="contact-text small">Mill House, Harbour Road,<br>Westbrook, Co.Kerry, Ireland.</span>
      </li>
    </ul>
  </section>

</main>
</body>
</html>
```